Free range pig farm business

We'd like a simple but elegant website for our new free range pig farm business.
Check out www.tallowcreekporkers.com.au and http://www.quorrihollow.com.au/
pages:
Home
About
Shop
Contact
Target Market(s)
People who would want to find out where they could buy our pork
Industry/Entity Type
Agribusiness
Number of Pages Required
4 page
Font styles to use
Other font styles liked:
- As per our logo
Requirements
Must have
- Ability for us to update weekly with new news and photos

```html
<!DOCTYPE html>
<html lang="en">
<head>
<meta charset="utf-8">
<title>Greenvale Free Range Pork</title>
<link href="https://fonts.googleapis.com/css2?family=Open+Sans:wght@400;600;700;800&family=Oswald:wght@500;600&display=swap" rel="stylesheet">
<style>
:root{
  --lime:#9dbb2b;
  --forest:#3c5a1d;
  --footer:#3d5722;
  --ink:#333333;
  --muted:#555555;
  --line:#dddddd;
  --white:#ffffff;
}
*{box-sizing:border-box;margin:0;padding:0}
html,body{width:1200px;height:2913px;overflow:hidden;background:var(--white)}
body{position:relative;font-family:"Open Sans",Arial,sans-serif;color:var(--ink)}
.abs{position:absolute}
.top-rule{left:0;top:0;width:1200px;height:6px;background:var(--forest)}
.top-rule-lime{left:0;top:6px;width:1200px;height:3px;background:var(--lime)}

.brand{left:132px;top:60px;width:240px;display:flex;align-items:center;gap:12px}
.brand-dot{width:34px;height:34px;border-radius:50%;background:var(--forest);flex:none}
.brand-name{font-weight:700;font-size:22px;line-height:1.15;color:var(--forest);letter-spacing:.5px;text-transform:uppercase}

.call{left:645px;top:66px;display:flex;gap:18px;align-items:center}
.call-label{font-size:13px;color:#777;letter-spacing:.5px}
.call-number{font-size:24px;color:var(--lime);line-height:1.1}
.search{left:924px;top:58px;width:144px;height:51px;border:1px solid #bbb;display:flex;align-items:center;padding-left:18px;gap:10px;font-size:10px;color:#888;letter-spacing:.5px}

.nav{left:540px;top:160px;height:36px;display:flex;align-items:center}
.nav a{font-size:15px;color:var(--ink);text-decoration:none;position:absolute;white-space:nowrap;top:9px}
.nav .home{background:var(--lime);color:var(--white);font-weight:600;left:0;top:0;width:91px;height:36px;display:flex;align-items:center;justify-content:center;gap:7px}

.hero{left:0;top:216px;width:1200px;height:454px;background:linear-gradient(100deg,#6b5638 0%,#8a7354 35%,#b79c84 62%,#8a7458 100%)}
.hero-title{left:130px;top:356px;font-family:"Oswald",Arial,sans-serif;font-weight:600;font-size:56px;color:var(--white);letter-spacing:.5px;line-height:1}
.hero-btn{left:130px;top:458px;width:187px;height:55px;border:3px solid var(--white);color:var(--white);font-weight:700;font-size:17px;display:flex;align-items:center;justify-content:center;gap:14px}
.dots{left:548px;top:599px;display:flex;gap:12px}
.dots span{width:13px;height:13px;border-radius:50%;background:var(--white)}
.dots span.open{background:transparent;border:2px solid var(--white)}
.hero-edge{left:0;top:668px}

.section-title{width:1200px;left:0;text-align:center;font-weight:800;font-size:27px;color:var(--forest);letter-spacing:.3px}
.rule{height:3px;background:var(--lime)}

.service{width:320px;text-align:center}
.service-ring{width:218px;height:218px;border:2px solid var(--lime);border-radius:50%;margin:0 auto;display:flex;align-items:center;justify-content:center}
.service h3{font-weight:600;font-size:24px;color:var(--forest);margin-top:66px}
.service p{font-size:14.5px;line-height:24px;color:var(--muted);margin-top:14px}
.btn-outline{display:inline-block;border:2px solid #333;font-size:11px;font-weight:700;padding:7px 12px;margin-top:20px;color:#333}

.card{width:292px;height:458px;border:1px solid var(--line);background:var(--white)}
.card-photo{width:100%;height:305px}
.card h4{font-weight:600;font-size:20px;color:var(--forest);margin:20px 0 0 30px}
.price{font-weight:700;font-size:20px;color:var(--lime);margin:4px 0 0 30px}
.shop-btn{margin:14px 0 0 30px;display:inline-flex;align-items:center;gap:10px;border:1px solid var(--lime);color:var(--lime);font-size:11px;font-weight:700;padding:6px 12px}

.sub{width:1200px;left:0;text-align:center;font-size:15px;color:#444}
.field{height:60px;border:1px solid #ccc;display:flex;align-items:center;gap:14px;padding-left:24px;font-size:13px;color:#666}
.signup{left:816px;top:2323px;width:132px;height:60px;background:var(--lime);color:var(--white);font-family:"Oswald",Arial,sans-serif;font-weight:600;font-size:21px;display:flex;align-items:center;justify-content:center;letter-spacing:.5px}

.footer{left:0;top:2484px;width:1200px;height:429px;background:var(--footer);color:var(--white)}
.footer-brand{left:132px;top:2610px;width:240px;display:flex;align-items:center;gap:12px}
.footer-brand .brand-dot{background:var(--white)}
.footer-brand .brand-name{color:var(--white)}
.contact-title{left:439px;top:2546px;font-size:13px;font-weight:700;letter-spacing:.5px}
.contact-row{left:437px;display:flex;align-items:center;gap:20px;font-size:12.5px;line-height:20px}
.contact-icon{width:30px;height:30px;border-radius:50%;background:var(--lime);display:flex;align-items:center;justify-content:center;flex:none}
.map{left:703px;top:2540px;width:365px;height:218px;background:linear-gradient(135deg,#e3e4df,#d6d8d0 55%,#e8e6dc)}
.footer-rule{left:132px;top:2818px;width:936px;height:1px;background:rgba(255,255,255,.25)}
.footer-links{left:132px;top:2858px;font-size:11px}
.copyright{right:132px;top:2858px;font-size:11px}
</style>
</head>
<body>
<div class="abs top-rule"></div>
<div class="abs top-rule-lime"></div>

<header>
  <div class="abs brand"><span class="brand-dot"></span><span class="brand-name">Greenvale Free Range Pork</span></div>
  <div class="abs call">
    <svg width="40" height="40" viewBox="0 0 40 40" fill="none" stroke="#3c5a1d" stroke-width="2.2"><path d="M10 6l6 7-3 4c2 4 5 7 9 9l4-3 7 6-4 5C18 34 6 22 5 10z"/><path d="M23 6a11 11 0 0 1 11 11M23 11a6 6 0 0 1 6 6"/></svg>
    <div><div class="call-label">CALL US</div><div class="call-number">(555).204.7731</div></div>
  </div>
  <div class="abs search">
    <svg width="10" height="10" viewBox="0 0 10 10" fill="none" stroke="#555" stroke-width="1.5"><circle cx="4" cy="4" r="3"/><path d="M6.5 6.5L9 9"/></svg>SEARCH
  </div>
  <nav class="abs nav">
    <a class="home" href="#"><svg width="13" height="12" viewBox="0 0 13 12" fill="#fff"><path d="M6.5 0L13 6h-2v6H8V8H5v4H2V6H0z"/></svg>Home</a>
    <a href="#" style="left:146px">About</a>
    <a href="#" style="left:256px">Service</a>
    <a href="#" style="left:375px">Shop</a>
    <a href="#" style="left:476px">Contact</a>
  </nav>
</header>

<section>
  <div class="abs hero" role="img" aria-label="Photo of a young pig standing in a muddy pen"></div>
  <h1 class="abs hero-title">PIG FARM BUSINESS</h1>
  <div class="abs hero-btn">READ MORE <svg width="7" height="10" viewBox="0 0 7 10" fill="#fff"><path d="M0 0l7 5-7 5z"/></svg></div>
  <div class="abs dots"><span></span><span class="open"></span><span></span><span></span><span></span></div>
  <svg class="abs hero-edge" width="1200" height="34" viewBox="0 0 1200 34">
    <rect x="0" y="0" width="1200" height="4" fill="#9dbb2b"/>
    <rect x="0" y="4" width="1200" height="5" fill="#3c5a1d"/>
    <path d="M566 9h68l-34 23z" fill="#3c5a1d"/>
    <path d="M583 2h34l-17 13z" fill="#9dbb2b"/>
  </svg>
</section>

<section>
  <h2 class="abs section-title" style="top:752px">OUR SERVICES</h2>
  <div class="abs rule" style="left:507px;top:799px;width:58px"></div>
  <div class="abs rule" style="left:577px;top:799px;width:118px"></div>

  <div class="abs service" style="left:110px;top:878px">
    <div class="service-ring"><div role="img" aria-label="Pig silhouette icon" style="width:140px;height:72px;border-radius:40px;background:#9dbb2b"></div></div>
    <h3>Pig Farm</h3>
    <p>There are many variations of passages<br>of Lorem Ipsum available.</p>
    <span class="btn-outline">READ MORE</span>
  </div>
  <div class="abs service" style="left:440px;top:878px">
    <div class="service-ring"><svg width="104" height="100" viewBox="0 0 104 100" fill="none" stroke="#9dbb2b" stroke-width="5" stroke-linejoin="round"><path d="M100 4L4 44l36 10 20 40z"/><path d="M40 54L100 4"/></svg></div>
    <h3>Our Mission</h3>
    <p>There are many variations of passages<br>of Lorem Ipsum available.</p>
    <span class="btn-outline">READ MORE</span>
  </div>
  <div class="abs service" style="left:778px;top:878px">
    <div class="service-ring"><svg width="104" height="110" viewBox="0 0 104 110" fill="none" stroke="#9dbb2b" stroke-width="5" stroke-linejoin="round"><path d="M6 106V44L30 8h44l24 36v62z"/><path d="M40 22h24v14H40zM28 62h48v44H28zM28 62l48 44M76 62l-48 44"/></svg></div>
    <h3>Manufacturing</h3>
    <p>There are many variations of passages<br>of Lorem Ipsum available.</p>
    <span class="btn-outline">READ MORE</span>
  </div>
</section>

<section>
  <h2 class="abs section-title" style="top:1467px">OUR FARM SHOP</h2>
  <div class="abs rule" style="left:487px;top:1524px;width:59px"></div>
  <div class="abs rule" style="left:557px;top:1524px;width:74px"></div>
  <div class="abs rule" style="left:643px;top:1524px;width:70px"></div>

  <div class="abs card" style="left:132px;top:1604px">
    <div class="card-photo" role="img" aria-label="Photo of raw pork steaks" style="background:linear-gradient(135deg,#b9434a,#d7767a 50%,#a83a40)"></div>
    <h4>Heading 1</h4><div class="price">$100.00</div>
    <span class="shop-btn">SHOP NOW <svg width="5" height="8" viewBox="0 0 5 8" fill="#9dbb2b"><path d="M0 0l5 4-5 4z"/></svg></span>
  </div>
  <div class="abs card" style="left:454px;top:1604px">
    <div class="card-photo" role="img" aria-label="Photo of a lunch box with pork and vegetables" style="background:linear-gradient(135deg,#a88a66,#6f7fb8 45%,#8a6a4a 75%,#c9b79a)"></div>
    <h4>Heading 2</h4><div class="price">$60.00</div>
    <span class="shop-btn">SHOP NOW <svg width="5" height="8" viewBox="0 0 5 8" fill="#9dbb2b"><path d="M0 0l5 4-5 4z"/></svg></span>
  </div>
  <div class="abs card" style="left:773px;top:1604px">
    <div class="card-photo" role="img" aria-label="Photo of a pig roasting on a spit" style="background:linear-gradient(135deg,#6e4a35,#9a3e22 45%,#7a2a18 75%,#8a7a6a)"></div>
    <h4>Heading 3</h4><div class="price">$300.00</div>
    <span class="shop-btn">SHOP NOW <svg width="5" height="8" viewBox="0 0 5 8" fill="#9dbb2b"><path d="M0 0l5 4-5 4z"/></svg></span>
  </div>
</section>

<section>
  <h2 class="abs section-title" style="top:2172px">NEWSLETTER SIGNUP</h2>
  <div class="abs rule" style="left:456px;top:2223px;width:175px"></div>
  <div class="abs rule" style="left:647px;top:2223px;width:97px"></div>
  <p class="abs sub" style="top:2259px">Get more details to signup!</p>
  <div class="abs field" style="left:243px;top:2323px;width:266px">
    <svg width="11" height="12" viewBox="0 0 11 12" fill="#999"><circle cx="5.5" cy="3.5" r="3"/><path d="M0 12c0-4 2.5-5.5 5.5-5.5S11 8 11 12z"/></svg>Name
  </div>
  <div class="abs field" style="left:528px;top:2323px;width:266px">
    <svg width="13" height="10" viewBox="0 0 13 10" fill="#999"><rect width="13" height="10" rx="1"/><path d="M0 1l6.5 5L13 1" stroke="#fff" fill="none"/></svg>E mail id
  </div>
  <div class="abs signup">SIGNUP!</div>
</section>

<footer>
  <div class="abs footer"></div>
  <div class="abs footer-brand"><span class="brand-dot"></span><span class="brand-name">Greenvale Free Range Pork</span></div>
  <div class="abs contact-title">CONTACT US</div>
  <div class="abs contact-row" style="top:2598px">
    <span class="contact-icon"><svg width="10" height="14" viewBox="0 0 10 14" fill="#3d5722"><path d="M5 0a5 5 0 0 1 5 5c0 4-5 9-5 9S0 9 0 5a5 5 0 0 1 5-5z"/><circle cx="5" cy="5" r="2" fill="#9dbb2b"/></svg></span>
    <span>418 Wattle Lane<br>Bellbrook, NSW 2440</span>
  </div>
  <div class="abs contact-row" style="top:2659px">
    <span class="contact-icon"><svg width="12" height="12" viewBox="0 0 12 12" fill="#3d5722"><path d="M2 0l3 3-1.5 2c1 2 2 3 3.5 3.5L9 7l3 3-2 2C5 12 0 7 0 2z"/></svg></span>
    <span>555.204.7731</span>
  </div>
  <div class="abs contact-row" style="top:2712px">
    <span class="contact-icon"><svg width="12" height="9" viewBox="0 0 12 9" fill="#3d5722"><rect width="12" height="9" rx="1"/><path d="M0 1l6 4 6-4" stroke="#9dbb2b" fill="none"/></svg></span>
    <span>hello@greenvalepork.com.au</span>
  </div>
  <div class="abs map" role="img" aria-label="Street map showing the farm location"></div>
  <div class="abs footer-rule"></div>
  <div class="abs footer-links" style="color:#fff">Home \ About \ Service \ Shop \ Contact</div>
  <div class="abs copyright" style="color:#fff">Copyrights @ 2016 All Rights Reserved</div>
</footer>
</body>
</html>
```